Brackenford Group Website

We have a newly established brand for a company with an existing portfolio of property. The company is corporate and professional and both owns and develops property. The website should reflect a professional and stable organisation. The website should showcase the existing properties (6), have a home page that describes the company and its activities and has a "about us" page. The website will be in Wordpress and we would like the code for all pages to be sent to us by the successful designer upon completion of the job.

sorry was called from the office on an urgent matter. To be fair on submitters, i need a couple more days to finalise reviews.

Contact Information for Business Card

Brackenford Logo on front
Black background with silver logo.

Coding

Number of Pages Required

5+ page

Colors

Designer to choose colors to be used in the design.

Requirements
Must have
• Text side of card should include
• Brackenford Property Group (as title in logo font)
• Employee Name (centered)
• Job Title (centered below name)
• Address 4 lines
• Email, mobile office phone, 3 lines
• website address (probably as footer)

```html
<!DOCTYPE html>
<html lang="en">
<head>
<meta charset="utf-8">
<title>Brackenford Property Group – Business Card</title>
<link rel="stylesheet" href="https://fonts.googleapis.com/css2?family=Lato:wght@300;400;700&family=Tinos&display=swap">
<style>
  :root {
    --page-top: #f4f4f4;
    --page-bottom: #e4e4e4;
    --card-white: #ffffff;
    --card-tint: #f3f3f3;
    --ink: #1d1d1d;
    --ink-soft: #333333;
    --band: #161616;
    --back-dark: #1a1a1a;
    --back-light: #2a2a2a;
    --silver: #c9c9c9;
    --white: #ffffff;
  }
  * { margin: 0; padding: 0; box-sizing: border-box; }
  html, body { width: 748px; height: 1200px; overflow: hidden; }
  body {
    position: relative;
    background: linear-gradient(180deg, var(--page-top), var(--page-bottom));
    font-family: "Lato", Arial, sans-serif;
    color: var(--ink);
  }
  .card {
    position: absolute;
    left: 40px;
    width: 668px;
    box-shadow: 0 2px 6px rgba(0,0,0,0.25);
    overflow: hidden;
  }
  .card-front { top: 39px; height: 455px; }
  .card-back { top: 633px; height: 447px; }

  .front-texture {
    position: absolute; inset: 0;
    background: linear-gradient(135deg, var(--card-white), var(--card-tint));
  }
  .top-rule {
    position: absolute; left: 0; top: 0; width: 100%; height: 6px;
    background: var(--band);
  }
  .card-title {
    position: absolute; left: 0; top: 30px; width: 100%; height: 42px;
    display: flex; align-items: center; justify-content: center; gap: 12px;
    font-family: "Tinos", "Times New Roman", serif;
    font-weight: 400; font-size: 35px; line-height: 42px; color: var(--ink);
  }
  .card-title::before, .card-title::after {
    content: ""; width: 64px; height: 1.5px; background: var(--ink);
  }
  .person-name {
    position: absolute; left: 0; top: 89px; width: 100%;
    text-align: center; font-weight: 700; font-size: 28px; line-height: 34px;
  }
  .person-role {
    position: absolute; left: 0; top: 130px; width: 100%;
    text-align: center; font-size: 21px; line-height: 26px; color: var(--ink-soft);
  }
  .address {
    position: absolute; left: 120px; top: 179px;
    font-size: 21.5px; line-height: 34.5px; font-style: normal;
  }
  .icon {
    position: absolute; width: 38px; height: 38px;
  }
  .icon-pin { left: 75px; top: 177px; }
  .icon-phone { left: 51px; top: 331px; }
  .icon-mail { left: 276px; top: 331px; }
  .contact-line {
    position: absolute; top: 334px; font-size: 21.5px; line-height: 32px;
  }
  .contact-phone { left: 98px; }
  .contact-email { left: 320px; }
  .footer-band {
    position: absolute; left: 0; bottom: 0; width: 100%; height: 48px;
    background: var(--band); color: var(--white);
    display: flex; align-items: center; justify-content: center;
    font-size: 21px;
  }

  .back-texture {
    position: absolute; inset: 0;
    background: radial-gradient(ellipse at 20% 20%, var(--back-light), var(--back-dark) 70%);
  }
  .brand-mark {
    position: absolute; left: 294px; top: 96px; width: 80px; height: 80px;
    background: var(--silver);
  }
  .brand-name {
    position: absolute; left: 0; top: 254px; width: 100%;
    text-align: center; font-weight: 400; color: var(--silver);
    font-size: 30px; line-height: 40px; letter-spacing: 3px;
    text-transform: uppercase;
  }

  .side-label {
    position: absolute; left: 0; width: 100%;
    text-align: center; font-weight: 300; font-size: 33px; color: var(--ink-soft);
  }
  .label-front { top: 514px; }
  .label-back { top: 1104px; }
</style>
</head>
<body>
  <section class="card card-front">
    <div class="front-texture" role="img" aria-label="Faint geometric line pattern on white card background"></div>
    <div class="top-rule"></div>
    <h1 class="card-title">Brackenford Property Group</h1>
    <p class="person-name">Colin Mercer</p>
    <p class="person-role">Director</p>

    <svg class="icon icon-pin" viewBox="0 0 38 38" aria-hidden="true">
      <polygon points="19,1 35,10 35,28 19,37 3,28 3,10" fill="var(--band)"/>
      <path d="M19 9c-4 0-7 3-7 7 0 5 7 12 7 12s7-7 7-12c0-4-3-7-7-7z" fill="var(--white)"/>
      <circle cx="19" cy="16" r="2.6" fill="var(--band)"/>
    </svg>
    <address class="address">
      Brackenford Group Ltd. Level 6, Harwood House<br>
      14 Harwood Lane. Northgate CBD. PO Box 2740<br>
      Marlow St. Northgate 1188
    </address>

    <svg class="icon icon-phone" viewBox="0 0 38 38" aria-hidden="true">
      <polygon points="19,1 35,10 35,28 19,37 3,28 3,10" fill="var(--band)"/>
      <path d="M13 11l4-1 2 5-2.5 1.5c1 2.5 3 4.5 5.5 5.5L23.5 19.5l5 2-1 4c-8 0-14.5-6.5-14.5-14.5z" fill="var(--white)"/>
    </svg>
    <span class="contact-line contact-phone">+64 9 555 0148</span>

    <svg class="icon icon-mail" viewBox="0 0 38 38" aria-hidden="true">
      <polygon points="19,1 35,10 35,28 19,37 3,28 3,10" fill="var(--band)"/>
      <rect x="11" y="13" width="16" height="12" rx="1" fill="var(--white)"/>
      <path d="M11 14l8 6 8-6" fill="none" stroke="var(--band)" stroke-width="1.6"/>
    </svg>
    <span class="contact-line contact-email">colin@brackenfordgroup.co.nz</span>

    <div class="footer-band">www.brackenfordgroup.co.nz</div>
  </section>
  <p class="side-label label-front">Front Side</p>

  <section class="card card-back">
    <div class="back-texture" role="img" aria-label="Subtle dark geometric line pattern on black card background"></div>
    <div class="brand-mark" aria-hidden="true"></div>
    <p class="brand-name">Brackenford Property Group</p>
  </section>
  <p class="side-label label-back">Back Side</p>
</body>
</html>
```